Painting services company needs a DL brochure about their services

We need a brochure describing our painting services including our logo and photos of work. The final design needs to be colourful, vibrant, and targeted to schools, aged care, commercial property maintenance clients.

```html
<!DOCTYPE html>
<html lang="en">
<head>
<meta charset="utf-8">
<title>Brightcoat Painters – DL Brochure</title>
<link href="https://fonts.googleapis.com/css2?family=Lilita+One&family=Open+Sans:wght@400;600;700;800&family=Roboto+Condensed:wght@300;400;700&display=swap" rel="stylesheet">
<style>
  :root{
    --backdrop:#a9a9a9;
    --blue:#1d6fb8;
    --navy:#123f8f;
    --band-blue:#2a5fc0;
    --yellow:#f6d80c;
    --orange:#f08a12;
    --white:#ffffff;
    --paper:#f1f0f0;
    --grey-arc:#b9bcc4;
    --ink-blue:#0f3d8c;
    --text-dark:#333840;
  }
  *{box-sizing:border-box;margin:0;padding:0}
  html,body{width:900px;height:1200px;overflow:hidden}
  body{background:radial-gradient(ellipse at center,#c2c2c2 0%,var(--backdrop) 70%,#8f8f8f 100%);font-family:"Open Sans",sans-serif;position:relative}
  .spread{position:absolute;left:50px;width:800px;height:566px;overflow:hidden;box-shadow:0 8px 24px rgba(0,0,0,.35)}
  .spread--outside{top:20px}
  .spread--inside{top:614px}
  .spread__art{position:absolute;inset:0;width:800px;height:566px;display:block}
  .abs{position:absolute}

  /* outside – panel 1 */
  .intro__headline{left:26px;top:26px;width:230px;font-family:"Roboto Condensed",sans-serif;font-weight:300;font-size:19px;line-height:1.22;color:var(--white);text-transform:uppercase}
  .intro__headline strong{font-weight:700;color:var(--yellow)}
  .intro__body{left:26px;top:140px;width:222px;font-size:8.4px;line-height:1.42;color:var(--white);text-align:justify}

  /* outside – panel 2 */
  .quote-pill{left:290px;top:88px;width:220px;height:52px;border-radius:26px;background:var(--navy);color:var(--white);font-weight:700;font-size:12.5px;line-height:1.3;text-align:center;padding-top:9px}
  .quote-pill em{font-style:italic;color:var(--yellow)}
  .contact{left:300px;width:200px;border:2px solid var(--navy);border-radius:9px;color:var(--navy);text-align:center;font-weight:600}
  .contact--phone{top:175px;height:34px;font-size:17px;font-weight:700;padding-top:5px}
  .contact--email{top:228px;height:26px;font-size:9.5px;padding-top:6px}
  .contact--post{top:273px;height:42px;font-size:9.5px;line-height:1.3;padding-top:6px}
  .contact--web{top:334px;height:26px;font-size:9.5px;padding-top:6px}
  .contact__icon{position:absolute;left:50%;top:-11px;transform:translateX(-50%);width:20px;height:20px;background:var(--yellow)}
  .social{top:380px;width:22px;height:22px;border:2px solid var(--navy);border-radius:50%}
  .social--one{left:376px}
  .social--two{left:404px}

  /* outside – cover */
  .brand{left:556px;top:30px;display:flex;align-items:center;gap:8px}
  .brand__square{width:16px;height:16px;background:var(--navy)}
  .brand__name{font-weight:800;font-size:15px;color:var(--navy);letter-spacing:.2px}
  .cover__title{left:560px;top:392px;width:220px;font-family:"Lilita One",sans-serif;font-size:33px;line-height:1.02;color:var(--white);text-transform:uppercase;text-align:center}
  .cover__title span{color:var(--yellow)}
  .cover__url{left:560px;top:522px;width:220px;text-align:center;color:var(--white);font-weight:600;font-size:11px}

  /* inside */
  .inside__title{left:120px;top:108px;width:320px;text-align:center;font-weight:800;font-size:24px;line-height:1.15;color:var(--white);text-transform:uppercase;text-shadow:0 2px 4px rgba(0,0,0,.45)}
  .service{width:240px}
  .service--commercial{left:24px;top:262px}
  .service--floor{left:290px;top:262px}
  .service--new{left:290px;top:400px}
  .service__heading{font-weight:800;font-size:11px;line-height:1.15;color:var(--ink-blue);text-transform:uppercase;margin-bottom:5px}
  .service__list{list-style:none}
  .service__list li{position:relative;padding-left:13px;font-size:8.8px;line-height:1.35;color:var(--text-dark);margin-bottom:1px}
  .service__list li::before{content:"";position:absolute;left:1px;top:3px;width:6px;height:3px;border-left:1.6px solid var(--ink-blue);border-bottom:1.6px solid var(--ink-blue);transform:rotate(-45deg)}
</style>
</head>
<body>

<section class="spread spread--outside" aria-label="Brochure outside spread">
  <svg class="spread__art" viewBox="0 0 800 566" xmlns="http://www.w3.org/2000/svg">
    <defs>
      <linearGradient id="yellowFade" x1="0" y1="0" x2="0" y2="1">
        <stop offset="0" stop-color="#f6d80c"/><stop offset="1" stop-color="#fbf2b8"/>
      </linearGradient>
      <linearGradient id="topBand" x1="0" y1="0" x2="0" y2="1">
        <stop offset="0" stop-color="#2a5fc0"/><stop offset="1" stop-color="#3a73d0"/>
      </linearGradient>
      <linearGradient id="tinPhoto" x1="0" y1="0" x2="1" y2="1">
        <stop offset="0" stop-color="#1f8fb0"/><stop offset=".5" stop-color="#0d4e6a"/><stop offset="1" stop-color="#06263a"/>
      </linearGradient>
      <linearGradient id="roomPhoto" x1="0" y1="0" x2="1" y2="1">
        <stop offset="0" stop-color="#f4f2ee"/><stop offset=".6" stop-color="#e6ddc8"/><stop offset="1" stop-color="#cfc3a6"/>
      </linearGradient>
    </defs>
    <rect x="0" y="0" width="267" height="566" fill="#1d6fb8"/>
    <rect x="267" y="0" width="266" height="566" fill="url(#yellowFade)"/>
    <!-- plain top band -->
    <path d="M267,0 H533 V52 C470,66 330,66 267,52 Z" fill="url(#topBand)"/>
    <path d="M0,300 C110,250 250,262 300,340 C330,400 332,490 340,566 L0,566 Z" fill="#f6d80c"/>
    <path role="img" aria-label="Photo: close-up of an open paint tin in blue tones" d="M0,308 C108,262 242,272 290,346 C318,404 320,490 326,566 L0,566 Z" fill="url(#tinPhoto)"/>
    <path d="M533,0 H800 V566 H533 Z" fill="#1d6fb8"/>
    <path d="M533,0 H800 V300 C740,300 690,270 650,230 C610,190 580,160 533,150 Z" fill="#f6d80c"/>
    <path d="M533,0 H800 V292 C742,292 694,262 656,224 C616,184 584,154 533,142 Z" fill="#f1f0f0"/>
    <path role="img" aria-label="Photo: paint pots, rollers and a stepladder in a freshly painted white room" d="M640,95 H800 V284 C748,284 700,256 662,218 C650,206 642,196 640,190 Z" fill="url(#roomPhoto)"/>
    <path d="M533,566 V390 C590,330 700,310 800,336 V566 Z" fill="#b9bcc4"/>
    <path d="M533,566 V398 C592,342 700,324 800,348 V566 Z" fill="#123f8f"/>
  </svg>

  <h2 class="abs intro__headline">We are a<br>family-run business<br><strong>with over 40 years'</strong><br>experience</h2>
  <p class="abs intro__body">We provide a full range of painting, decorating and protective coatings services through specialised divisions. This is the best way to guarantee that our clients are getting the best level of customer service possible from the enquiry and quotation to the provision of the right staff with the right skills and attitude to carry out the required preparation and application.</p>

  <p class="abs quote-pill">Call or email us <em>NOW</em><br>to get a <em>FAST QUOTE!</em></p>
  <p class="abs contact contact--phone">1300 555 018
    <svg class="contact__icon" viewBox="0 0 20 20"><circle cx="10" cy="10" r="9" fill="#f6d80c" stroke="#123f8f" stroke-width="1.5"/><path d="M7,5 L9,8 L8,9 C8.5,10.5 9.5,11.5 11,12 L12,11 L15,13 L14,15 C10,15 5,10 5,6 Z" fill="#123f8f"/></svg>
  </p>
  <p class="abs contact contact--email">hello@brightcoatpainters.com
    <svg class="contact__icon" viewBox="0 0 20 20"><rect x="3" y="5" width="14" height="10" fill="#f6d80c" stroke="#123f8f" stroke-width="1.5"/><path d="M3,5 L10,11 L17,5" fill="none" stroke="#123f8f" stroke-width="1.5"/></svg>
  </p>
  <p class="abs contact contact--post">P.O. Box 410<br>Hillbrook, NSW 2290
    <svg class="contact__icon" viewBox="0 0 20 20"><path d="M10,18 C6,13 4,10 4,7.5 A6,6 0 0 1 16,7.5 C16,10 14,13 10,18 Z" fill="#f6d80c" stroke="#123f8f" stroke-width="1.5"/><circle cx="10" cy="7.5" r="2" fill="#123f8f"/></svg>
  </p>
  <p class="abs contact contact--web">www.brightcoatpainters.com.au
    <svg class="contact__icon" viewBox="0 0 20 20"><circle cx="10" cy="10" r="7.5" fill="#f6d80c" stroke="#123f8f" stroke-width="1.5"/><path d="M2.5,10 H17.5 M10,2.5 C6,6 6,14 10,17.5 M10,2.5 C14,6 14,14 10,17.5" fill="none" stroke="#123f8f" stroke-width="1.2"/></svg>
  </p>
  <span class="abs social social--one" aria-label="Social link"></span>
  <span class="abs social social--two" aria-label="Social link"></span>

  <div class="abs brand"><span class="brand__square"></span><span class="brand__name">Brightcoat Painters</span></div>
  <h1 class="abs cover__title">Friendly<br><span>Painting</span><br>Contractors</h1>
  <p class="abs cover__url">www.brightcoatpainters.com.au</p>
</section>

<section class="spread spread--inside" aria-label="Brochure inside spread">
  <svg class="spread__art" viewBox="0 0 800 566" xmlns="http://www.w3.org/2000/svg">
    <defs>
      <linearGradient id="paperFade" x1="0" y1="0" x2="1" y2="0">
        <stop offset="0" stop-color="#e6e6e6"/><stop offset=".5" stop-color="#fafafa"/><stop offset="1" stop-color="#ececec"/>
      </linearGradient>
      <linearGradient id="corridorPhoto" x1="0" y1="0" x2="1" y2="1">
        <stop offset="0" stop-color="#8a7a2a"/><stop offset=".5" stop-color="#c6b348"/><stop offset="1" stop-color="#6f6420"/>
      </linearGradient>
      <linearGradient id="cansPhoto" x1="0" y1="0" x2="1" y2="1">
        <stop offset="0" stop-color="#3aa0c8"/><stop offset=".35" stop-color="#d04a7a"/><stop offset=".65" stop-color="#9a4ec0"/><stop offset="1" stop-color="#52c04a"/>
      </linearGradient>
      <linearGradient id="interiorPhoto" x1="0" y1="0" x2="1" y2="1">
        <stop offset="0" stop-color="#9a9a8c"/><stop offset="1" stop-color="#4a4a44"/>
      </linearGradient>
    </defs>
    <rect x="0" y="0" width="800" height="566" fill="url(#paperFade)"/>
    <path role="img" aria-label="Photo: freshly painted school corridor in warm yellow light" d="M0,60 C120,20 300,10 533,0 V150 C420,170 260,190 0,205 Z" fill="url(#corridorPhoto)"/>
    <path d="M0,0 H533 V0 C300,10 120,20 0,60 Z" fill="#ececec"/>
    <path d="M0,66 C120,26 300,14 533,4" fill="none" stroke="#ffffff" stroke-width="6"/>
    <!-- plain orange band -->
    <path d="M0,202 C260,188 420,168 533,148 V166 C420,186 260,206 0,220 Z" fill="#f08a12"/>
    <rect role="img" aria-label="Photo: open tins of brightly coloured paint seen from above" x="20" y="430" width="230" height="136" rx="4" fill="url(#cansPhoto)" opacity=".85"/>
    <rect x="533" y="0" width="267" height="566" fill="#1d6fb8"/>
    <path d="M533,0 H570 C545,120 560,260 620,380 C660,460 700,520 720,566 H533 Z" fill="#f5f5f5"/>
    <g stroke="#f6d80c" stroke-width="3">
      <rect role="img" aria-label="Photo: painted factory interior with overhead services" x="585" y="30" width="185" height="105" rx="14" fill="url(#interiorPhoto)"/>
      <rect role="img" aria-label="Photo: newly painted classroom with desks" x="605" y="160" width="170" height="100" rx="14" fill="#c8ccd2"/>
      <rect role="img" aria-label="Photo: large hall with freshly coated floor" x="620" y="285" width="160" height="100" rx="14" fill="#5a554c"/>
      <rect role="img" aria-label="Photo: retail store interior after repainting" x="635" y="410" width="150" height="100" rx="14" fill="#b8906a"/>
    </g>
  </svg>

  <h2 class="abs inside__title">Specialist Painting<br>Contractors</h2>

  <div class="abs service service--commercial">
    <h3 class="service__heading">Commercial &amp; Industrial<br>Painting Services</h3>
    <ul class="service__list">
      <li>Pressure cleaning of building facades</li>
      <li>Painting of broad areas and trim to commercial interiors and exteriors</li>
      <li>Corrosion repairs and protective coatings for steel</li>
      <li>On-site spray painting</li>
      <li>Texture coatings</li>
      <li>After-hours and weekends available</li>
    </ul>
  </div>

  <div class="abs service service--floor">
    <h3 class="service__heading">Floor Preparation and<br>Coating Services</h3>
    <ul class="service__list">
      <li>Diamond grinding</li>
      <li>Shot blasting</li>
      <li>Glue and surface removal</li>
      <li>Epoxy and polyurethane coatings</li>
      <li>Anti-slip coatings</li>
      <li>Epoxy floors for warehouse and workshop</li>
    </ul>
  </div>

  <div class="abs service service--new">
    <h3 class="service__heading">New Construction<br>Painting Services</h3>
    <ul class="service__list">
      <li>Painting of new buildings</li>
      <li>Internals and externals</li>
      <li>Spray painting and texture coatings</li>
    </ul>
  </div>
</section>

</body>
</html>
```